Offshore Energy Projects Management Consultancy needs a business card design

Logo available. We provide teams to deliver engineering consultancy, project management and delivery teams mainly in the offshore renewables sector. The company is all about bringing the right people to a project to deliver the scope.

The business card will be used for all staff.

The business card should be quite simple, vibrant and uncluttered but convey experience, enthusiasm and integration.

Target Market(s)

Energy Project Developers and Tier 1 construction companies

Contact Information for Business Card

Logo should be on the back of the card. I'm happy for the designer to play with the colour of the logo and background colour.

Front of the card should convey all the must have information in a clear and professional manner but without being overly traditional.

Colors

Designer to choose colors to be used in the design.

Requirements
Must have
• Land Line Tel Number, Mobile Tel Number, Email, business address, web address.

```html
<!DOCTYPE html>
<html lang="en">
<head>
<meta charset="utf-8">
<title>Seaward Delivery Group – Business Card</title>
<link href="https://fonts.googleapis.com/css2?family=Lato:wght@400;700&display=swap" rel="stylesheet">
<style>
  :root {
    --backdrop: #2c2c2c;
    --card-white: #ededed;
    --blue-deep: #1e77bd;
    --blue-bright: #29a8e0;
    --ink: #444444;
    --ink-soft: #6a6a6a;
    --rule: #9a9a9a;
    --white: #ffffff;
  }
  * { margin: 0; padding: 0; box-sizing: border-box; }
  html, body {
    width: 1200px;
    height: 1200px;
    overflow: hidden;
    background: var(--backdrop);
    font-family: "Lato", sans-serif;
  }
  .canvas { position: relative; width: 1200px; height: 1200px; }

  .card {
    position: absolute;
    top: 310px;
    height: 594px;
  }
  .card-front {
    left: 234px;
    width: 364px;
    background: var(--card-white);
    text-align: center;
    color: var(--ink);
  }
  .card-back {
    left: 627px;
    width: 369px;
    background: linear-gradient(to bottom, var(--blue-bright) 0, var(--blue-bright) 360px, var(--blue-deep) 360px);
  }

  .brand-name {
    position: absolute;
    top: 172px;
    left: 0;
    width: 100%;
    font-size: 24px;
    font-weight: 700;
    letter-spacing: 1px;
    color: var(--ink-soft);
  }
  .brand-mark {
    position: absolute;
    top: 96px;
    left: 162px;
    width: 40px;
    height: 40px;
    border-radius: 50%;
    background: var(--blue-deep);
  }

  .person-name {
    position: absolute;
    top: 302px;
    left: 0;
    width: 100%;
    font-size: 24px;
    font-weight: 700;
    letter-spacing: 0.5px;
    color: var(--blue-deep);
  }
  .person-name .surname { color: var(--blue-bright); }
  .person-role {
    position: absolute;
    top: 328px;
    left: 0;
    width: 100%;
    font-size: 17px;
  }

  .contact-icons {
    position: absolute;
    top: 366px;
    left: 78px;
    width: 213px;
    height: 24px;
  }

  .contact-list {
    position: absolute;
    top: 395px;
    left: 0;
    width: 100%;
    list-style: none;
    font-size: 17px;
    line-height: 21.7px;
  }
  .divider {
    position: absolute;
    top: 493px;
    left: 78px;
    width: 213px;
    height: 1px;
    background: var(--rule);
  }
  .address {
    position: absolute;
    top: 505px;
    left: 0;
    width: 100%;
    font-size: 17px;
    line-height: 21.5px;
    font-style: normal;
  }

  .back-name {
    position: absolute;
    top: 256px;
    left: 0;
    width: 100%;
    text-align: center;
    font-size: 62px;
    font-weight: 700;
    color: var(--white);
    letter-spacing: 1px;
  }
  .back-web {
    position: absolute;
    top: 516px;
    left: 0;
    width: 100%;
    text-align: center;
    font-size: 16px;
    letter-spacing: 1.5px;
    color: var(--white);
  }
</style>
</head>
<body>
<main class="canvas">

  <section class="card card-front">
    <div class="brand-mark" aria-hidden="true"></div>
    <div class="brand-name">SEAWARD DELIVERY GROUP</div>

    <div class="person-name">DANIEL <span class="surname">HART</span></div>
    <div class="person-role">Managing Director</div>

    <svg class="contact-icons" viewBox="0 0 213 24" aria-hidden="true">
      <line x1="0" y1="12" x2="47" y2="12" stroke="#9a9a9a" stroke-width="1"/>
      <line x1="166" y1="12" x2="213" y2="12" stroke="#9a9a9a" stroke-width="1"/>
      <!-- landline -->
      <rect x="53" y="1" width="22" height="22" rx="4" fill="#1e77bd"/>
      <path d="M57 11 q7 -6 14 0 v2 h-3 v-2 h-8 v2 h-3z" fill="#fff"/>
      <rect x="59" y="13" width="10" height="6" rx="1" fill="#fff"/>
      <!-- mobile -->
      <rect x="81" y="1" width="22" height="22" rx="4" fill="#1e77bd"/>
      <rect x="87" y="5" width="10" height="14" rx="1.5" fill="none" stroke="#fff" stroke-width="1.6"/>
      <circle cx="92" cy="16.5" r="0.9" fill="#fff"/>
      <!-- email -->
      <rect x="109" y="1" width="22" height="22" rx="4" fill="#1e77bd"/>
      <rect x="113" y="7" width="14" height="10" fill="none" stroke="#fff" stroke-width="1.5"/>
      <path d="M113 7 l7 6 l7 -6" fill="none" stroke="#fff" stroke-width="1.5"/>
      <!-- web -->
      <rect x="137" y="1" width="22" height="22" rx="4" fill="#1e77bd"/>
      <circle cx="148" cy="12" r="6.5" fill="none" stroke="#fff" stroke-width="1.5"/>
      <ellipse cx="148" cy="12" rx="2.8" ry="6.5" fill="none" stroke="#fff" stroke-width="1.2"/>
      <line x1="141.5" y1="12" x2="154.5" y2="12" stroke="#fff" stroke-width="1.2"/>
    </svg>

    <ul class="contact-list">
      <li>444 555 6688</li>
      <li>444 555 6688</li>
      <li>info@youremail.com</li>
      <li>www.websitename.com</li>
    </ul>
    <div class="divider"></div>
    <address class="address">421, Address line here<br>Country Name,45452</address>
  </section>

  <section class="card card-back">
    <div class="back-name">SEAWARD</div>
    <div class="back-web">www.websitename.com</div>
  </section>

</main>
</body>
</html>
```